Endocrinologist needs new stationery

I have a logo from MarkForge and now need stationery with the new logo.

Address: Suite 4, 282 Falcon Street, Kelvale, VIC 3988
Phone: 03 9417 2253
Fax: 03 9417 2255
Website: www.drmaylacorwen.com.au
Email: admin@drmaylacorwen.com.au

```html
<!DOCTYPE html>
<html lang="en">
<head>
<meta charset="utf-8">
<title>Dr Mayla Corwen – Stationery</title>
<link rel="stylesheet" href="https://fonts.googleapis.com/css2?family=Tinos:wght@400;700&family=Arimo:wght@400;700&family=Roboto+Condensed:wght@400;700&display=swap">
<style>
  :root {
    --blue: #2e6fa2;
    --plum: #734f6b;
    --ink: #1d1d1d;
    --paper: #ffffff;
    --backdrop: #d5dbde;
    --serif: "Tinos", "Times New Roman", serif;
    --sans: "Arimo", Arial, sans-serif;
    --cond: "Roboto Condensed", Arial, sans-serif;
  }
  * { box-sizing: border-box; margin: 0; padding: 0; }
  html, body { width: 1200px; height: 699px; overflow: hidden; }
  body { background: var(--backdrop); position: relative; font-family: var(--serif); color: var(--ink); }

  .piece { position: absolute; background: var(--paper); overflow: hidden; }
  .wave { position: absolute; left: 0; bottom: 0; width: 100%; display: block; }
  .wave .band { fill: var(--blue); }
  .wave .gap { fill: var(--paper); }
  .wave .accent { fill: var(--plum); }

  .brand { font-family: var(--serif); color: var(--blue); font-weight: 400; white-space: nowrap; position: absolute; }
  address { font-style: normal; }

  .contact { list-style: none; font-family: var(--serif); }
  .contact li { display: flex; align-items: center; white-space: nowrap; }
  .contact svg { fill: var(--blue); color: var(--blue); flex: none; }

  /* Letterhead */
  .letterhead { left: 73px; top: 60px; width: 424px; height: 600px; }
  .letterhead .brand { left: 23px; top: 36px; font-size: 16px; }
  .letterhead .sender { position: absolute; right: 23px; top: 20px; text-align: right; font-size: 7px; line-height: 10px; }
  .letterhead .sender .contact { margin-top: 7px; }
  .letterhead .sender .contact li { justify-content: flex-end; gap: 6px; }
  .letterhead .sender svg { width: 6px; height: 6px; }
  .letterhead .rule { position: absolute; left: 22px; top: 89px; width: 379px; height: 1px; background: var(--plum); }
  .letterhead .rule::after { content: ""; position: absolute; right: 0; top: 0; width: 107px; height: 2px; background: var(--blue); }
  .recipient { position: absolute; left: 23px; top: 120px; font-family: var(--sans); }
  .person-name { font-family: var(--cond); font-size: 20px; line-height: 22px; }
  .person-name .first { color: var(--blue); font-weight: 700; }
  .person-name .last { color: var(--plum); }
  .person-role { font-size: 8px; font-weight: 700; margin-top: 1px; }
  .recipient .contact { font-family: var(--sans); font-size: 7.5px; line-height: 10px; margin-top: 12px; }
  .recipient .contact li { gap: 4px; }
  .recipient .contact svg { width: 6px; height: 6px; }
  .letter-date { position: absolute; right: 23px; top: 128px; font-family: var(--sans); font-weight: 700; font-size: 10px; }
  .letter-body { position: absolute; left: 23px; top: 213px; width: 379px; font-family: var(--sans); font-size: 8.9px; line-height: 12.1px; text-align: justify; }
  .letter-body p + p { margin-top: 12px; }
  .signature { position: absolute; left: 23px; top: 423px; width: 145px; height: 45px; background: linear-gradient(90deg, rgba(90,90,100,0.10), rgba(90,90,100,0.22), rgba(90,90,100,0.08)); border-radius: 4px; }
  .signatory { position: absolute; left: 23px; top: 474px; font-family: var(--sans); }
  .letterhead .wave { height: 44px; }

  /* Envelope front */
  .envelope-front { left: 519px; top: 62px; width: 346px; height: 153px; }
  .envelope-front .brand { right: 9px; top: 12px; font-size: 13px; }
  .envelope-front .sender { position: absolute; left: 241px; top: 80px; font-size: 6px; line-height: 8.3px; }
  .envelope-front .contact { margin-top: 5px; }
  .envelope-front .contact li { gap: 4px; }
  .envelope-front .contact svg { width: 5px; height: 5px; }
  .envelope-front .wave { height: 34px; }

  /* Envelope back */
  .envelope-back { left: 522px; top: 232px; width: 344px; height: 152px; }
  .envelope-back .flap { position: absolute; left: 2px; top: 0; width: 340px; height: 52px; border-radius: 0 0 12px 12px; background: var(--paper); box-shadow: 0 3px 6px rgba(0,0,0,0.12); }

  /* Card front */
  .card-front { left: 882px; top: 63px; width: 268px; height: 153px; background: var(--blue); }
  .card-front .brand { left: 0; right: 0; top: 62px; text-align: center; color: var(--paper); font-size: 19px; }

  /* Card back */
  .card-back { left: 882px; top: 232px; width: 268px; height: 153px; }
  .card-back .brand { left: 9px; top: 68px; font-size: 13px; }
  .divider { position: absolute; width: 1px; background: var(--blue); }
  .card-back .divider { left: 134px; top: 27px; height: 98px; }
  .card-back .details { position: absolute; left: 157px; top: 33px; }
  .card-name { font-family: var(--serif); font-weight: 700; }
  .card-name .first { color: var(--blue); }
  .card-name .last { color: var(--plum); }
  .card-back .card-name { font-size: 12.5px; line-height: 14px; }
  .card-back .specialty { font-size: 6.5px; line-height: 8px; }
  .card-back .address { font-size: 6.3px; line-height: 9px; margin-top: 6px; }
  .card-back .contact { font-size: 6.3px; line-height: 9.2px; margin-top: 6px; }
  .card-back .contact li { gap: 4px; }
  .card-back .contact svg { width: 5px; height: 5px; }
  .card-back .wave { height: 34px; }

  /* Large card */
  .card-large { left: 537px; top: 432px; width: 592px; height: 197px; }
  .card-large .brand { left: 44px; top: 78px; font-size: 24px; }
  .card-large .divider { left: 296px; top: 11px; height: 154px; }
  .card-large .details { position: absolute; left: 357px; top: 16px; }
  .card-large .card-name { font-size: 21px; line-height: 24px; }
  .card-large .specialty { font-size: 11px; line-height: 13px; margin-top: 2px; }
  .card-large .address { font-size: 11.5px; line-height: 15.5px; margin-top: 9px; }
  .card-large .contact { font-size: 11.5px; line-height: 15.4px; margin-top: 10px; }
  .card-large .contact li { gap: 6px; }
  .card-large .contact svg { width: 10px; height: 10px; }
  .card-large .wave { height: 58px; }
  .social { position: absolute; left: 23px; top: 171px; display: flex; gap: 6px; list-style: none; }
  .social li { width: 9px; height: 9px; border-radius: 50%; background: var(--paper); }
</style>
</head>
<body>

<svg width="0" height="0" style="position:absolute" aria-hidden="true">
  <defs>
    <symbol id="icon-phone" viewBox="0 0 10 10"><path d="M2 1 L3.6 1 L4.3 3 L3.2 3.8 C3.8 5 5 6.2 6.2 6.8 L7 5.7 L9 6.4 L9 8 C9 8.6 8.5 9 8 9 C4.5 9 1 5.5 1 2 C1 1.5 1.4 1 2 1Z"/></symbol>
    <symbol id="icon-fax" viewBox="0 0 10 10"><path d="M1 4 H9 V9 H1Z M2.5 1 H6.5 V3.5 H2.5Z M2 5 V6 H3 V5Z M4 5 V6 H5 V5Z M6 5 V6 H7 V5Z" fill-rule="evenodd"/></symbol>
    <symbol id="icon-globe" viewBox="0 0 10 10"><circle cx="5" cy="5" r="4" fill="none" stroke="currentColor"/><path d="M1 5 H9 M5 1 C3 3 3 7 5 9 C7 7 7 3 5 1" fill="none" stroke="currentColor" stroke-width="0.8"/></symbol>
    <symbol id="icon-mail" viewBox="0 0 10 10"><path d="M1 3 H9 V8.5 H1Z M1 3 L5 6 L9 3" fill="none" stroke="currentColor" stroke-width="1"/></symbol>
    <symbol id="wave-shape" viewBox="0 0 100 100" preserveAspectRatio="none">
      <path class="band" d="M0 0 C35 40 70 58 100 40 V100 H0Z"/>
      <path class="gap" d="M30 43 C60 70 85 68 100 50 V74 C80 85 55 80 30 43Z"/>
      <path class="accent" d="M33 43 C60 64 85 62 100 50 V64 C80 74 58 68 33 43Z"/>
    </symbol>
  </defs>
</svg>

<!-- Letterhead -->
<section class="piece letterhead">
  <div class="brand">Dr Mayla Corwen</div>
  <div class="sender">
    <address>Suite 4, 282 Falcon Street,<br>Kelvale, VIC 3988</address>
    <ul class="contact">
      <li>03 9417 2253 <svg><use href="#icon-phone"/></svg></li>
      <li>03 9417 2255 <svg><use href="#icon-fax"/></svg></li>
      <li>www.drmaylacorwen.com.au <svg><use href="#icon-globe"/></svg></li>
      <li>admin@drmaylacorwen.com.au <svg><use href="#icon-mail"/></svg></li>
    </ul>
  </div>
  <div class="rule"></div>

  <div class="recipient">
    <div class="person-name"><span class="first">Renata</span> <span class="last">Voskova</span></div>
    <div class="person-role">Founder &amp; CEO</div>
    <ul class="contact">
      <li><svg><use href="#icon-phone"/></svg>(817) 555-0142</li>
      <li><svg><use href="#icon-globe"/></svg>www.mockwebsite.com</li>
      <li><svg><use href="#icon-mail"/></svg>info@mockwebsite.com</li>
    </ul>
  </div>
  <div class="letter-date">August-05-2019</div>

  <div class="letter-body">
    <p>Lorem ipsum dolor sit amet, consectetuer adipiscing elit, sed diam nonummy nibh euismod tincidunt ut laoreet dolore magna aliquam erat volutpat. Ut wisi enim ad minim veniam, quis nostrud exerci tation ullamcorper suscipit lobortis</p>
    <p>Lorem ipsum dolor sit amet, cons ectetuer adipiscing elit, sed diam nonummy nibh euismod tincidunt ut laoreet dolore magna aliquam erat volutpat. Ut wisi enim ad minim veniam, quis nostrud exerci tation ullamcorper suscipit lobortis nisl ut aliquip ex ea commodo consequat. Lorem ipsum dolor sit amet, consectetuer olutpat. Ut wisi enim ad minim veniam, quis nostrud exerci tation ullamcorper suscipit lobortis nisl ut aliquip ex ea commodo consequat. Duis autem</p>
    <p>vel eum iriure dolor in hendrerit in vulputate velit esse molestie consequat, vel illum dolore eu feugiat nulla facilisis at vero eros et accumsan et iusto odio dignissim qui blandit praesent luptatum zzril delenit augue duis dolore te feugait nulla facilisi. Lorem ipsum dolor sit amet, cons ectetuer adipiscing elit, sed diam nonummy nibh euismod tincidunt ut laoreet dolore magna aliquam erat volutpat. Ut wisi enim .</p>
  </div>

  <div class="signature" role="img" aria-label="Handwritten signature of the director"></div>
  <div class="signatory">
    <div class="person-name"><span class="first">Milena</span> <span class="last">Draskova</span></div>
    <div class="person-role">Director</div>
  </div>

  <svg class="wave" aria-hidden="true"><use href="#wave-shape"/></svg>
</section>

<!-- Envelope front -->
<section class="piece envelope-front">
  <div class="brand">Dr Mayla Corwen</div>
  <div class="sender">
    <address>Suite 4, 282 Falcon Street,<br>Kelvale, VIC 3988</address>
    <ul class="contact">
      <li><svg><use href="#icon-phone"/></svg>03 9417 2253</li>
      <li><svg><use href="#icon-fax"/></svg>03 9417 2255</li>
      <li><svg><use href="#icon-globe"/></svg>www.drmaylacorwen.com.au</li>
      <li><svg><use href="#icon-mail"/></svg>admin@drmaylacorwen.com.au</li>
    </ul>
  </div>
  <svg class="wave" aria-hidden="true"><use href="#wave-shape"/></svg>
</section>

<!-- Envelope back -->
<section class="piece envelope-back">
  <div class="flap"></div>
</section>

<!-- Business card front -->
<section class="piece card-front">
  <div class="brand">Dr Mayla Corwen</div>
</section>

<!-- Business card back -->
<section class="piece card-back">
  <div class="brand">Dr Mayla Corwen</div>
  <div class="divider"></div>
  <div class="details">
    <div class="card-name"><span class="first">DrMayla</span> <span class="last">Corwen</span></div>
    <div class="specialty">ENDOCRINOLOGY</div>
    <address class="address">Suite 4, 282 Falcon Street,<br>Kelvale, VIC 3988</address>
    <ul class="contact">
      <li><svg><use href="#icon-phone"/></svg>03 9417 2253</li>
      <li><svg><use href="#icon-fax"/></svg>03 9417 2255</li>
      <li><svg><use href="#icon-globe"/></svg>www.drmaylacorwen.com.au</li>
      <li><svg><use href="#icon-mail"/></svg>admin@drmaylacorwen.com.au</li>
    </ul>
  </div>
  <svg class="wave" aria-hidden="true"><use href="#wave-shape"/></svg>
</section>

<!-- Large card -->
<section class="piece card-large">
  <div class="brand">Dr Mayla Corwen</div>
  <div class="divider"></div>
  <div class="details">
    <div class="card-name"><span class="first">DrMayla</span> <span class="last">Corwen</span></div>
    <div class="specialty">ENDOCRINOLOGY</div>
    <address class="address">Suite 4, 282 Falcon Street,<br>Kelvale, VIC 3988</address>
    <ul class="contact">
      <li><svg><use href="#icon-phone"/></svg>03 9417 2253</li>
      <li><svg><use href="#icon-fax"/></svg>03 9417 2255</li>
      <li><svg><use href="#icon-globe"/></svg>www.drmaylacorwen.com.au</li>
      <li><svg><use href="#icon-mail"/></svg>admin@drmaylacorwen.com.au</li>
    </ul>
  </div>
  <svg class="wave" aria-hidden="true"><use href="#wave-shape"/></svg>
  <ul class="social" aria-label="Social links">
    <li></li><li></li><li></li><li></li><li></li>
  </ul>
</section>

</body>
</html>
```